Business Card Design Project

Hi,

We are a new modern sheet metal business and I require a business card for our sales reps.

The card should be double sided and standout in a crowd.

I have attached our logo and our website is www.folvik.com.au.

Please ask if you have any further questions
Updates

hi everyone, 

I'm wondering if we can try to lighten the cards mood.  Everyone is using black and I'm not sure how that would be accepted in real life.

Gregory

Reason: Still No receiving what I was hoping for.

Industry/Entity Type

Business

Requirements
Must have
• double sided

```html
<!DOCTYPE html>
<html lang="en">
<head>
<meta charset="utf-8">
<title>Folvik Sheetmetal – Business Card</title>
<link rel="stylesheet" href="https://fonts.googleapis.com/css2?family=Didact+Gothic&family=Questrial&display=swap">
<style>
  :root {
    --navy: #1d2a78;
    --navy-deep: #0f1750;
    --ink-grey: #6b6b6b;
    --soft-grey: #9a9a9a;
    --card-white: #ffffff;
    --stage: #d9d9d9;
    --back-text: #e8ebf5;
    --back-sub: #aab3d6;
  }
  * { box-sizing: border-box; margin: 0; padding: 0; }
  html, body { width: 1200px; height: 871px; overflow: hidden; }
  body {
    background: var(--stage);
    font-family: "Didact Gothic", "Questrial", sans-serif;
    display: flex;
    align-items: center;
    justify-content: center;
    gap: 40px;
  }
  .card {
    width: 540px;
    height: 309px;
    border-radius: 4px;
    position: relative;
    box-shadow: 0 6px 18px rgba(0,0,0,0.18);
  }
  /* Front side */
  .card-front {
    background: var(--card-white);
    padding: 34px 30px 30px 34px;
    display: grid;
    grid-template-columns: 1fr 210px;
    column-gap: 20px;
  }
  .brand { display: flex; align-items: center; gap: 10px; }
  .brand-square { width: 22px; height: 22px; background: var(--navy); flex: none; }
  .brand-name {
    font-family: "Questrial", sans-serif;
    font-size: 27px;
    color: var(--navy);
    letter-spacing: 1px;
    line-height: 1;
  }
  .tagline {
    margin-top: 14px;
    font-size: 12.5px;
    color: var(--soft-grey);
    white-space: nowrap;
  }
  .tagline .sep { color: var(--navy); font-weight: bold; margin: 0 4px; }
  .person { margin-top: 60px; padding-left: 62px; }
  .person-name {
    font-family: "Questrial", sans-serif;
    color: var(--navy);
    font-size: 20px;
    font-weight: bold;
    letter-spacing: 0.5px;
    -webkit-text-stroke: 0.5px var(--navy);
  }
  .person-role { color: var(--ink-grey); font-size: 17px; margin-top: 2px; }
  .contact { font-size: 15px; color: var(--ink-grey); line-height: 1.35; padding-top: 22px; }
  .contact .label { color: var(--navy); }
  .contact-group + .contact-group { margin-top: 16px; }
  .contact-group.spaced { margin-top: 34px; }
  /* Back side */
  .card-back {
    background: linear-gradient(135deg, #3a4a9a 0%, var(--navy) 40%, var(--navy-deep) 100%);
    display: flex;
    flex-direction: column;
    align-items: center;
    justify-content: center;
    gap: 16px;
  }
  .card-back .brand-square { background: var(--back-text); width: 30px; height: 30px; }
  .card-back .brand-name { color: var(--back-text); font-size: 38px; }
  .card-back .tagline { color: var(--back-sub); margin-top: 0; font-size: 14px; }
  .card-back .tagline .sep { color: var(--back-text); }
</style>
</head>
<body>
  <section class="card card-front" aria-label="Business card, front">
    <div class="identity">
      <div class="brand">
        <span class="brand-square"></span>
        <span class="brand-name">FOLVIK SHEETMETAL</span>
      </div>
      <p class="tagline">Flashings<span class="sep">|</span>Gutter<span class="sep">|</span>Rainwater Goods</p>
      <div class="person">
        <p class="person-name">DANIEL HARPER</p>
        <p class="person-role">Sales Manager</p>
      </div>
    </div>
    <div class="contact">
      <div class="contact-group">
        <p>24 Quartz Road</p>
        <p>Wacol Q 4076</p>
      </div>
      <div class="contact-group">
        <p><span class="label">Phone:</span> 3555 0142</p>
        <p><span class="label">Fax:</span> 3555 0143</p>
      </div>
      <div class="contact-group">
        <p>www.folvik.com.au</p>
      </div>
      <div class="contact-group spaced">
        <p><span class="label">Mobile:</span> 0400 555 218</p>
        <p><span class="label">Email:</span> info@folvik.com.au</p>
      </div>
    </div>
  </section>

  <section class="card card-back" aria-label="Business card, back">
    <div class="brand">
      <span class="brand-square"></span>
      <span class="brand-name">FOLVIK SHEETMETAL</span>
    </div>
    <p class="tagline">Flashings<span class="sep">|</span>Gutter<span class="sep">|</span>Rainwater Goods</p>
  </section>
</body>
</html>
```